Morvela Aesthetic Doctor

I require an elegant, luxurious looking business card for my aesthetic business. I am a doctor and that will set me aside from competitors. I am planning to provide home and spa based treatments to clients with high expectations. I have attached my logo.

```html
<!DOCTYPE html>
<html lang="en">
<head>
<meta charset="utf-8">
<title>Morvela Aesthetic Doctor – Business Card</title>
<link rel="stylesheet" href="https://fonts.googleapis.com/css2?family=Marcellus&family=Arimo:wght@400;700&family=Kalam:wght@400;700&display=swap">
<style>
  :root {
    --page: #ffffff;
    --brand-blue: #0f6fc2;
    --brand-blue-dark: #0b5fae;
    --silver: #c4bdb6;
    --white: #ffffff;
    --text-grey: #6f7377;
    --text-dark: #333639;
    --rule: #eef0f2;
    --ghost: #e9f1f8;
  }
  * { box-sizing: border-box; margin: 0; padding: 0; }
  html, body {
    width: 1200px; height: 806px; overflow: hidden;
    background: var(--page);
  }
  .canvas { position: relative; width: 1200px; height: 806px; }

  .card {
    position: absolute;
    width: 523px; height: 334px;
    overflow: hidden;
  }

  /* Front */
  .card--front {
    left: 127px; top: 107px;
    background: var(--brand-blue);
    text-align: center;
  }
  .front__mark {
    position: absolute; left: 216px; top: 44px;
  }
  .front__name {
    position: absolute; left: 0; right: 0; top: 150px;
    font-family: "Marcellus", serif;
    color: var(--silver);
    line-height: 1;
  }
  .front__name-main { display: block; font-size: 72px; letter-spacing: 2px; }
  .front__name-sub { display: block; font-size: 29px; letter-spacing: 1px; margin-top: 6px; }
  .front__tagline {
    position: absolute; left: 0; right: 0; top: 261px;
    font-family: "Kalam", cursive;
    font-weight: 700;
    font-size: 11px;
    color: var(--white);
  }

  /* Back */
  .card--back {
    left: 559px; top: 362px;
    background: var(--white);
    border: 1px solid var(--rule);
  }
  .back__ghost { position: absolute; left: 20px; top: 50px; }
  .back__identity {
    position: absolute; right: 60px; top: 60px;
    text-align: right;
    font-family: "Arimo", sans-serif;
  }
  .back__name {
    font-size: 13px; font-weight: 700; color: var(--brand-blue);
  }
  .back__credentials {
    font-size: 8px; font-weight: 400; margin-left: 5px; color: var(--brand-blue);
  }
  .back__qualification {
    margin-top: 5px; font-size: 8.5px; color: var(--text-grey);
  }
  .back__services {
    position: absolute; left: 0; right: 0; top: 148px;
    display: flex; justify-content: center; gap: 7px;
    font-family: "Arimo", sans-serif; font-size: 8.5px; color: var(--text-grey);
    list-style: none;
    padding-left: 90px;
  }
  .back__services li + li::before { content: "."; margin-right: 7px; }
  .back__tagline {
    position: absolute; left: 90px; right: 0; top: 166px;
    text-align: center;
    font-family: "Kalam", cursive; font-size: 10px;
    color: var(--brand-blue);
  }
  .back__social {
    position: absolute; left: 240px; top: 194px;
    display: flex; gap: 7px;
  }
  .back__social span {
    width: 15px; height: 15px; border-radius: 50%;
    background: var(--brand-blue-dark);
  }
  .back__rule {
    position: absolute; left: 0; right: 0; top: 243px;
    border-top: 1px solid var(--rule);
  }
  .back__contacts {
    position: absolute; left: 0; right: 0; top: 254px;
    display: flex; justify-content: center; gap: 14px;
    padding-left: 20px;
    list-style: none;
    font-family: "Arimo", sans-serif; font-size: 10px; color: var(--text-dark);
  }
  .contact { display: flex; align-items: center; gap: 8px; }
  .contact__icon {
    width: 22px; height: 22px; border-radius: 50%;
    background: var(--brand-blue);
    display: flex; align-items: center; justify-content: center;
  }
</style>
</head>
<body>
<main class="canvas">

  <section class="card card--front" aria-label="Business card front">
    <svg class="front__mark" width="92" height="92" viewBox="0 0 92 92" aria-hidden="true">
      <circle cx="46" cy="46" r="43" fill="none" stroke="var(--silver)" stroke-width="3"/>
    </svg>
    <h1 class="front__name">
      <span class="front__name-main">MORVELA</span>
      <span class="front__name-sub">AESTHETIC DOCTOR</span>
    </h1>
    <p class="front__tagline">Home and Spa Based Treatments</p>
  </section>

  <section class="card card--back" aria-label="Business card back">
    <svg class="back__ghost" width="190" height="190" viewBox="0 0 190 190" aria-hidden="true">
      <circle cx="95" cy="95" r="90" fill="none" stroke="var(--ghost)" stroke-width="3"/>
    </svg>

    <div class="back__identity">
      <p class="back__name">Dr. Elise Varden<span class="back__credentials">MRCPCH MD</span></p>
      <p class="back__qualification">Australasian Diploma of Aesthetic Medicine</p>
    </div>

    <ul class="back__services">
      <li>Dermal injectables</li>
      <li>Plasma facials</li>
      <li>Microneedling</li>
      <li>Skin boosters</li>
      <li>Excessive sweating</li>
    </ul>

    <p class="back__tagline">Home and Spa Based Treatments</p>

    <div class="back__social" aria-label="Social media">
      <span></span><span></span>
    </div>

    <div class="back__rule"></div>

    <ul class="back__contacts">
      <li class="contact">
        <span class="contact__icon">
          <svg width="12" height="12" viewBox="0 0 24 24" aria-hidden="true">
            <path d="M6.6 10.8a15 15 0 0 0 6.6 6.6l2.2-2.2c.3-.3.7-.4 1-.2 1.1.4 2.3.6 3.6.6.6 0 1 .4 1 1V20c0 .6-.4 1-1 1A17 17 0 0 1 3 4c0-.6.4-1 1-1h3.5c.6 0 1 .4 1 1 0 1.3.2 2.5.6 3.6.1.3 0 .7-.2 1z" fill="var(--white)"/>
          </svg>
        </span>
        0800 555 019
      </li>
      <li class="contact">
        <span class="contact__icon">
          <svg width="12" height="12" viewBox="0 0 24 24" aria-hidden="true">
            <rect x="3" y="5" width="18" height="14" rx="1.5" fill="none" stroke="var(--white)" stroke-width="2"/>
            <path d="M3.5 6l8.5 7 8.5-7" fill="none" stroke="var(--white)" stroke-width="2"/>
          </svg>
        </span>
        elise@morvela.co.nz
      </li>
      <li class="contact">
        <span class="contact__icon">
          <svg width="12" height="12" viewBox="0 0 24 24" aria-hidden="true">
            <circle cx="12" cy="12" r="9" fill="none" stroke="var(--white)" stroke-width="2"/>
            <ellipse cx="12" cy="12" rx="4" ry="9" fill="none" stroke="var(--white)" stroke-width="1.6"/>
            <path d="M3 12h18" stroke="var(--white)" stroke-width="1.6"/>
          </svg>
        </span>
        www.morvela.co.nz
      </li>
    </ul>
  </section>

</main>
</body>
</html>
```